RM Tomás Rivera (Business Card)

Hi designers, in this work, I'm looking for an sophisticated stylish, elegant and proffesional personal card. We have a laboratory of pathology automated, with equipments high quality.
In this web the designers, have created my business logo, the name is "RM Tomás Rivera"
In our lab, we principal work is to prepare the biopsies for further diagnostic of diseases like cancer, tumors, etc.
I need that the first face, only having my complete logo (Rm Tomás Rivera, Laboratorio de procesamiento Histologico)
The overleaf, could repeat the same logo, like water logo.
In this face, I need to say: My full data:

Técnico en Anatomía Patológica
Tomás Rivera Ibarra M.P 47203
Av. Paredes Luján 418 - 2do piso - Instituto Marbel.
Córdoba, Argentina
(0351) 154820937
rivera.tomas@correolab.example

with respect the colors of card, use your imagination, the original logo color is violet, I haven't chosen a color base for the card.

attached pictures are examples of cards I like your DESIGN.
Attached too, the original logo to my company.

the size of card are:
horizontal: 9cm
vertical: 5,5cm

any question that you have, not doubt to question me,
Hand to work!

Industry/Entity Type

Laboratory

Requirements
Must have
• designers sophisticated, not simples, like show the images attached

```html
<!DOCTYPE html>
<html lang="es">
<head>
<meta charset="utf-8">
<title>Tomás Rivera — Tarjeta personal</title>
<link rel="stylesheet" href="https://fonts.googleapis.com/css2?family=Roboto+Condensed:ital,wght@0,300;0,400;0,700;1,300&display=swap">
<style>
  :root {
    --stage: #ecebef;
    --card: #ffffff;
    --violet: #5e2a8f;
    --violet-soft: #8c63b3;
    --grey: #8d8d92;
    --grey-dark: #5f5f64;
    --line: #d6d2dc;
  }
  * { margin: 0; padding: 0; box-sizing: border-box; }
  html, body {
    width: 1200px;
    height: 1023px;
    overflow: hidden;
    background: var(--stage);
    font-family: "Roboto Condensed", Arial, sans-serif;
  }
  .sheet {
    width: 1200px;
    height: 1023px;
    display: flex;
    flex-direction: column;
    align-items: center;
    justify-content: center;
    gap: 56px;
  }
  .card {
    width: 700px;
    height: 428px;
    background: var(--card);
    border-radius: 14px;
    box-shadow: 0 10px 28px rgba(40, 20, 60, 0.14);
    position: relative;
    overflow: hidden;
  }

  /* Front */
  .card--front {
    display: flex;
    align-items: center;
    justify-content: center;
  }
  .brand {
    display: flex;
    flex-direction: column;
    align-items: flex-start;
  }
  .brand__row {
    display: flex;
    align-items: center;
    gap: 18px;
  }
  .brand__mark {
    width: 54px;
    height: 54px;
    border: 2px solid var(--violet-soft);
    border-radius: 50%;
  }
  .brand__name {
    font-weight: 300;
    font-size: 30px;
    letter-spacing: 0.42em;
    color: var(--violet);
    text-transform: uppercase;
  }
  .brand__rule {
    width: 100%;
    height: 1px;
    background: var(--line);
    margin: 14px 0 10px;
  }
  .brand__tagline {
    font-weight: 400;
    font-size: 19px;
    letter-spacing: 0.02em;
    color: var(--grey);
    text-transform: uppercase;
  }

  /* Back */
  .card--back {
    padding: 70px 64px;
    display: flex;
    flex-direction: column;
  }
  .contact__name {
    font-weight: 700;
    font-size: 34px;
    color: var(--violet);
    line-height: 1.1;
  }
  .contact__role {
    font-style: italic;
    font-weight: 300;
    font-size: 20px;
    color: var(--violet-soft);
    margin-top: 6px;
  }
  .contact__rule {
    width: 80px;
    height: 2px;
    background: var(--violet);
    margin: 26px 0 22px;
  }
  .contact__line {
    font-weight: 400;
    font-size: 19px;
    color: var(--grey-dark);
    line-height: 1.55;
  }
  .contact__line--accent { color: var(--violet); }
</style>
</head>
<body>
<main class="sheet">
  <section class="card card--front" aria-label="Frente de la tarjeta">
    <div class="brand">
      <div class="brand__row">
        <span class="brand__mark" aria-hidden="true"></span>
        <span class="brand__name">Tomás Rivera</span>
      </div>
      <div class="brand__rule"></div>
      <p class="brand__tagline">Laboratorio de procesamiento histológico</p>
    </div>
  </section>

  <section class="card card--back" aria-label="Dorso de la tarjeta">
    <h1 class="contact__name">Tomás Rivera Ibarra M.P 47203</h1>
    <p class="contact__role">Técnico en Anatomía Patológica</p>
    <div class="contact__rule"></div>
    <p class="contact__line">Av. Paredes Luján 418 - 2do piso - Instituto Marbel.</p>
    <p class="contact__line">Córdoba, Argentina</p>
    <p class="contact__line contact__line--accent">(0351) 154820937</p>
    <p class="contact__line contact__line--accent">rivera.tomas@correolab.example</p>
  </section>
</main>
</body>
</html>
```